Print & digital package needed for technology firm

We need a package of coordinating marketing materials for our technology business. We offer technology solutions to midsized organizations, including data center, outsourced IT, and technology consulting. Find more information on our website, www.pexlora.com. Design is the main concern, we can modify the text ongoing to best reflect our company’s offerings. The design should communicate technology expertise and strategic thinking. Our website is currently being updated with a “flat design” theme and we’d like design of these items to be flat, fresh, modern, and professional, without being boring.
Please use attached logo - can send in .ai/.eps/.psd/etc. Fonts in logo are Futura, Futura Book, and Lato. Please use pexLORA blue, #0372bb.
Please find attached one of our product flyers for one of the computers we lease. Fonts used are Roboto Slab (partial to this font) & Lato. Also attached copy of our business card design.
Taglines we have used include “Does IT hear what troubles you?” and “IT made simple” although we are open to new ideas.
Would like final products to be available in editable files - .psd/.tif/.ai/etc.

- 1 PowerPoint template
- 1 leaderboard ad (digital, 72dpi)
- 1 medium rectangle ad 300x250 (digital, 72dpi)
- 1 full page ad 8x11 (print, 300dpi)
- 1 half-page ad horizontal (print, 300dpi)
- 1 letterhead template
- 1 proposal front-page

There is potential for further graphic/print design opportunities for our business as well.

All, thank you for your assistance in understanding the budget process with this type of design contest - we have updated the project's budget to reflect the items we are requesting.

Please email mvarga at pexlora.com with inquiries or comments. Thank you.

Designers,

Due to an oversight, our project was listed as "refundable" - this has been corrected and changed to committed payment.
To enter into this contest, please pick 2-3 items from the list of desired materials (ads, powerpoint, letterhead, etc.) It is not necessary to submit all items which will be part of the final package to be considered for the contest.

Thank you. Please contact mvarga@pexlora.com for questions.
Best,
Mimi

CEOs, CFOs, CIOs, COOs - college+ educated, 30-60, professional.

```html
<!DOCTYPE html>
<html lang="en">
<head>
<meta charset="utf-8">
<title>Pexlora stationery set</title>
<link href="https://fonts.googleapis.com/css2?family=Lato:wght@400;700&family=Arimo:wght@400;700&display=swap" rel="stylesheet">
<style>
:root{
  --brand-blue:#3e6fb5;
  --brand-blue-light:#5a86c6;
  --ink:#222;
  --ink-soft:#555;
  --paper:#ffffff;
  --ground:#ececec;
  --ghost:#eef0f4;
  --on-blue:#dbe5f3;
}
*{margin:0;padding:0;box-sizing:border-box}
html,body{width:800px;height:1200px;overflow:hidden;background:var(--ground)}
body{position:relative;font-family:"Arimo",Arial,sans-serif;color:var(--ink)}
.brand{font-family:"Lato",sans-serif;font-weight:700;color:var(--brand-blue);white-space:nowrap;line-height:1}
.services{font-family:"Lato",sans-serif;font-size:7px;color:var(--ink-soft);white-space:nowrap}

/* Letterhead */
.letterhead{position:absolute;left:59px;top:104px;width:428px;height:609px;background:var(--paper);overflow:hidden}
.letterhead .band{position:absolute;left:0;bottom:0;width:100%;height:150px;background:var(--ghost)}
.letterhead .brand{position:absolute;left:33px;top:28px;font-size:26px}
.letterhead .services{position:absolute;left:34px;top:60px}
.letterhead .sender{position:absolute;left:318px;top:20px;font-family:"Lato",sans-serif;font-size:6px;line-height:8px;color:var(--ink-soft)}
.letterhead .sender p+p{margin-top:5px}
.letter{position:absolute;left:33px;top:102px;width:370px;font-size:8.6px;line-height:10.4px}
.letter .recipient{margin-bottom:24px}
.letter .salutation{margin-bottom:9px}
.letter h2{font-size:8.6px;font-weight:700;text-transform:uppercase}
.letter p.body{margin-bottom:10px}
.signature{width:96px;height:42px;margin:4px 0 4px;background:linear-gradient(135deg,#f2f2f2,#e0e0e0)}

/* Business cards */
.card{position:absolute;left:543px;width:184px;height:105px;overflow:hidden}
.card-front{top:111px;background:var(--brand-blue)}
.card-front .band{position:absolute;left:0;top:0;width:60px;height:100%;background:var(--brand-blue-light);opacity:.5}
.card-front .brand{position:absolute;left:38px;top:37px;font-size:18px;color:#fff}
.card-front .services{position:absolute;left:39px;top:60px;font-size:5px;color:var(--on-blue)}
.card-back{top:246px;background:var(--paper)}
.card-back::after{content:"";position:absolute;right:0;top:0;width:9px;height:100%;background:var(--brand-blue)}
.card-back .brand{position:absolute;right:20px;top:10px;font-size:11px}
.card-back .services{position:absolute;right:20px;top:23px;font-size:3.5px}
.card-back .person{position:absolute;left:13px;top:24px;font-family:"Lato",sans-serif}
.card-back .person b{display:block;font-size:7.5px;color:var(--ink)}
.card-back .person span{display:block;font-size:4.5px;line-height:5.5px;color:var(--ink-soft);margin-top:2px}
.card-back .details{position:absolute;top:56px;font-family:"Lato",sans-serif;font-size:4.6px;line-height:6px;color:var(--ink-soft)}
.card-back .details.left{left:13px}
.card-back .details.right{left:88px}
.card-back .web{position:absolute;left:88px;top:90px;font-family:"Lato",sans-serif;font-size:4.6px;color:var(--ink-soft)}

/* Mobile screen */
.mobile-screen{position:absolute;left:545px;top:420px;width:106px;height:173px;background:var(--brand-blue);overflow:hidden}
.mobile-screen .brand{position:absolute;left:7px;top:9px;font-size:11px;color:#fff}
.mobile-screen .services{position:absolute;left:7px;top:23px;font-size:3.5px;color:var(--on-blue)}
.mobile-screen h1{position:absolute;right:7px;top:36px;width:70px;font-family:"Lato",sans-serif;font-weight:700;font-size:10px;line-height:10px;color:#fff;text-align:right;text-transform:uppercase}
.mobile-screen .team-photo{position:absolute;left:0;bottom:0;width:100%;height:95px;background:linear-gradient(180deg,#aebfd6 0%,#dfe5ee 55%,#3c4a5e 100%)}

/* Envelope */
.envelope{position:absolute;left:59px;top:771px;width:448px;height:216px;background:var(--brand-blue);overflow:hidden}
.envelope .band{position:absolute;left:0;top:0;width:100%;height:140px;background:var(--brand-blue-light);opacity:.45}
.envelope .brand{position:absolute;left:22px;top:164px;font-size:20px;color:#fff}
.envelope .services{position:absolute;left:23px;top:189px;font-size:5.5px;color:var(--on-blue)}
.envelope .sender{position:absolute;left:355px;top:164px;font-family:"Lato",sans-serif;font-size:4.5px;line-height:6px;color:var(--on-blue)}
.envelope .sender p+p{margin-top:3px}
</style>
</head>
<body>

<section class="letterhead">
  <div class="band" aria-hidden="true"></div>
  <div class="brand">Pexlora</div>
  <div class="services">IT Consulting | Managed Services | Data Center</div>
  <div class="sender">
    <p>418 Meridian Court Suite 210<br>Fairbrook, MD 20911</p>
    <p>Phone: 301-555-0142<br>Fax: 301-555-0187</p>
    <p>www.pexlora.com</p>
  </div>
  <article class="letter">
    <p class="recipient"><b>Reference No:</b> 70017397 239998432<br>Ms. L Okafor<br>12 Willowbank Lane<br>Hartfield<br>3120</p>
    <p class="salutation">Dear Mr Halvorsen,</p>
    <h2>Lorem ipsum dolor sit amet, consectetur adipiscing elit.</h2>
    <p class="body">Sed aliquam augue hendrerit, ornare lectus sit amet, volutpat sem. Sed sollicitudin augue et augue egestas, in molestie dolor blandit. Etiam suscipit ante eros, id tempor dolor mattis vitae. Sed a molestie libero.</p>
    <p class="body">Morbi blandit sapien non sapien facilisis pulvinar. Quisque ornare felis ultrices neque aliquet sagittis tincidunt eleifend tellus. Maecenas ullamcorper ante justo, ut ornare sapien iaculis sodales. Duis vulputate lectus ut sem lacinia, viverra semper sem porta. Class aptent taciti sociosqu ad litora torquent per conubia nostra, per inceptos himenaeos. Pellentesque habitant morbi tristique senectus et netus et malesuada fames ac turpis egestas. Pellentesque ligula neque, hendrerit eu molestie a, mattis eget magna. Nulla vel mi eget urna cursus sollicitudin in nec risus. Etiam tellus lectus, sodales nec nulla ac, luctus rhoncus orci. Phasellus nec commodo massa. Duis a consectetur turpis. Aenean sed nisi purus. Cras aliquet congue augue quis tristique. Praesent vel convallis urna. Integer convallis vehicula lorem, sit amet consectetur urna. Pellentesque ultrices tellus est, varius volutpat dolor tincidunt non.</p>
    <p class="body">Sed nisl nunc, bibendum eu ante eu, suscipit faucibus erat. Cras tellus, adipiscing at rutrum in, consectetur quis risus. Phasellus a mattis metus. Nam non facilisis magna. Nunc sagittis sit amet tellus at ullamcorper. Quisque ornare purus nec leo commodo accumsan. Nunc rutrum in mauris sed semper.</p>
    <p>Yours Sincerly</p>
    <div class="signature" role="img" aria-label="Handwritten signature of Owen Radley"></div>
    <p>Owen Radley<br>Marketing Manager</p>
  </article>
</section>

<section class="card card-front">
  <div class="band" aria-hidden="true"></div>
  <div class="brand">Pexlora</div>
  <div class="services">IT Consulting | Managed Services | Data Center</div>
</section>

<section class="card card-back">
  <div class="brand">Pexlora</div>
  <div class="services">IT Consulting | Managed Services | Data Center</div>
  <div class="person"><b>Mimi Varga</b><span>Marketing Specialist<br>mvarga@pexlora.com</span></div>
  <div class="details left">Direct: 240-555-0163<br>Mobile: 412-555-0119</div>
  <div class="details right">418 Meridian Court Suite 210<br>Fairbrook, MD 20911<br><br>Phone: 301-555-0142<br>Fax: 301-555-0187</div>
  <div class="web">www.pexlora.com</div>
</section>

<section class="mobile-screen">
  <div class="brand">Pexlora</div>
  <div class="services">IT Consulting | Managed Services | Data Center</div>
  <h1>Making IT work for your business</h1>
  <div class="team-photo" role="img" aria-label="Photo of a business team gathered around a laptop in an office"></div>
</section>

<section class="envelope">
  <div class="band" aria-hidden="true"></div>
  <div class="brand">Pexlora</div>
  <div class="services">IT Consulting | Managed Services | Data Center</div>
  <div class="sender">
    <p>418 Meridian Court Suite 210<br>Fairbrook, MD 20911</p>
    <p>Phone: 301-555-0142<br>Fax: 301-555-0187</p>
    <p>www.pexlora.com</p>
  </div>
</section>

</body>
</html>
```